Real Estate Agent needs business card design

We have logo designed already, want to have business card designed. Very interested in those smaller size business card as they look very trendy. Business name is called VORENDA REALTY

```html
<!DOCTYPE html>
<html lang="en">
<head>
<meta charset="utf-8">
<title>Vorenda Realty – Business Card</title>
<link href="https://fonts.googleapis.com/css2?family=Tinos:wght@400;700&display=swap" rel="stylesheet">
<style>
  :root {
    --gold: #c9a46e;
    --ink: #1c1c1c;
    --paper: #ffffff;
    --backdrop: #2b2b2d;
  }
  * { box-sizing: border-box; margin: 0; padding: 0; }
  html, body {
    width: 1200px; height: 925px; overflow: hidden;
    background: var(--backdrop);
    font-family: "Tinos", "Times New Roman", serif;
  }
  .sheet {
    position: relative; width: 1200px; height: 925px;
    display: flex; justify-content: center; align-items: center; gap: 90px;
  }
  .card {
    position: relative; width: 340px; height: 580px; overflow: hidden;
    box-shadow: 0 10px 30px rgba(0,0,0,.45);
  }

  /* Front */
  .card--front { background: var(--gold); }
  .front-brand {
    position: absolute; left: 34px; bottom: 92px;
    color: var(--paper); font-size: 30px; font-weight: 700; line-height: 1.05;
    letter-spacing: .5px;
  }
  .front-web {
    position: absolute; left: 34px; bottom: 54px;
    color: var(--ink); font-size: 16px;
  }

  /* Back */
  .card--back { background: var(--paper); }
  .corner-arc {
    position: absolute; top: -62px; right: -62px;
    width: 124px; height: 124px; border-radius: 50%; background: var(--gold);
  }
  .agent { position: absolute; left: 150px; top: 92px; }
  .agent-name { color: var(--gold); font-size: 19px; font-weight: 700; }
  .agent-role { color: var(--ink); font-size: 14px; margin-top: 2px; }
  .brand-disc {
    position: absolute; left: 50%; top: 200px; transform: translateX(-50%);
    width: 196px; height: 196px; border-radius: 50%; background: var(--gold);
    display: flex; align-items: center; justify-content: center; text-align: center;
  }
  .brand-name {
    color: var(--paper); font-size: 21px; font-weight: 400; letter-spacing: 1.5px; line-height: 1.25;
  }
  .contact {
    position: absolute; left: 34px; top: 440px;
    color: var(--ink); font-size: 16px; line-height: 1.3;
  }
  .contact-address { margin-left: 22px; margin-bottom: 2px; }
  .contact-row { display: flex; align-items: center; gap: 6px; }
  .contact-row svg { width: 16px; height: 16px; flex: none; }
  .contact-web { margin-left: 22px; }
  .contact-web .accent { color: var(--gold); }
</style>
</head>
<body>
<main class="sheet">
  <section class="card card--front" aria-label="Card front">
    <div class="front-brand">VORENDA<br>REALTY</div>
    <div class="front-web">www.vorendarealty.com.au</div>
  </section>

  <section class="card card--back" aria-label="Card back">
    <div class="corner-arc"></div>
    <div class="agent">
      <div class="agent-name">Hannah Lowell</div>
      <div class="agent-role">Senior Property Consultant</div>
    </div>
    <div class="brand-disc">
      <span class="brand-name">VORENDA<br>REALTY</span>
    </div>
    <div class="contact">
      <div class="contact-address">7C, 48 Harbour Parade,<br>Lane Cove, NSW 2066</div>
      <div class="contact-row">
        <svg viewBox="0 0 16 16" aria-hidden="true">
          <circle cx="8" cy="8" r="8" fill="var(--gold)"/>
          <path d="M5.2 4.2l1.6-.4.9 2-1 .8c.5 1.1 1.3 1.9 2.3 2.4l.8-1 2 .9-.4 1.6c-3.3.2-6.4-2.9-6.2-6.3z" fill="#fff"/>
        </svg>
        <span>0400 512 739</span>
      </div>
      <div class="contact-row">
        <svg viewBox="0 0 16 16" aria-hidden="true">
          <circle cx="8" cy="8" r="8" fill="var(--gold)"/>
          <g fill="none" stroke="#fff" stroke-width="1">
            <circle cx="8" cy="8" r="4.5"/>
            <ellipse cx="8" cy="8" rx="2" ry="4.5"/>
            <path d="M3.5 8h9"/>
          </g>
        </svg>
        <span>www.<span class="accent">vorendarealty</span>.com.au</span>
      </div>
    </div>
  </section>
</main>
</body>
</html>
```